Mosswood Chiropractic Web Design

We need a fully operating Web site design INCLUDING the code for a Chiropractic Clinic based in Auckland New Zealand to target people from different financial backgrounds.

We need 4 Pages as followed:
1. Home: includes Slideshow of the clinic, General information about chiropractic, option for "Request an appointment", and it would be nice to have a picture on the top right side of the header and the clinic's name and logo on the top left side. on the bottom right we would like a small section for "Testimonial" (A good example: http://www.fernlightstudio.example/ )
(A good example for slide show is: http://www.bektora.example.nz/)
(A good example for the header is: http://www.spinewellpraxis.example/)

2. About Us: this section will include the background information of the company, and a section for our staff (which will includes a photo and description of each person/staff which can be changedanytime)
(a good example: http://www.harbourlanechiro.example.nz/)

3. Contact: includes location, map, contact numbers, email, and a contact box (A good example: http://www.fernlightstudio.example/contact/)

4. Services: includes our products, adjustment equipment, chiropractic products for sale, few pictures of patients while under chiropractic care/adjustment tables

We would also like to add "social networking" options on the bottom left side of every page (Facebook, twitter, Blog, Google+)

Please check the following links to get a feel of our favorite designs:
http://www.spinewellpraxis.example/
http://www.harbourlanechiro.example.nz/
http://www.bektora.example.nz/
http://www.brindlechiropracticclinic.example/
http://www.stillwoven.example.nz/
http://www.pqr.example.nz/index-1.html
http://home.keelbrookchiro.example.nz/home/

we would like to have full access to the back-end- admin of the website to be able to change and add any pictures or texts.
Updates

Hi Lovely Designer,

thank you so much for your proposed designs. We just uploaded the original source file of our logo, for you all to have access on it to facilitate your work. 

Enjoy your day

Orla

Target Market(s)

People with different financial background as well as we are located in the artistic part of town, so appealing to those crowd is important to us.

Industry/Entity Type

Financial

Requirements
Must have
• 1.color similar to the logo or darker colors (Dark and rich colors are prefered)
2. more artistic than a basic doctors' clinic
3. I would like the opening of the web to bring art, tranquility and peaceful images into mind
Should not have
• Not bombarded with lots of info and pics in one page, not too busy and crowded

```html
<!DOCTYPE html>
<html lang="en">
<head>
<meta charset="utf-8">
<title>Mosswood Chiropractic</title>
<link rel="stylesheet" href="https://fonts.googleapis.com/css2?family=Open+Sans:wght@400;600&family=Arimo:ital,wght@0,400;0,700;1,400&family=Roboto+Condensed:wght@700&display=swap">
<style>
:root{
  --navy:#0a2b5a;
  --navy-deep:#061f45;
  --panel:#0d3a73;
  --box:#0f4a86;
  --green:#9bc31c;
  --white:#ffffff;
  --nav-grey:#e9e9e9;
  --footer-top:#e2e2e2;
  --footer-bottom:#f7f7f7;
  --star:#f2a37b;
  --icon-dark:#2b2b2b;
}
*{margin:0;padding:0;box-sizing:border-box}
html,body{width:1088px;height:1200px;overflow:hidden}
body{background:var(--navy);font-family:"Arimo",Arial,sans-serif;color:var(--white);position:relative}
.abs{position:absolute}

.brand{left:92px;top:28px;display:flex;align-items:center;gap:10px}
.brand-dot{width:26px;height:26px;border-radius:50%;background:var(--green)}
.brand-name{font-family:"Open Sans",sans-serif;font-size:24px;font-weight:400;color:#d7e3ef;letter-spacing:.5px}

.call{right:108px;top:38px;text-align:right}
.call-label{font-family:"Open Sans",sans-serif;font-size:17px;color:var(--white)}
.call-number{display:flex;align-items:center;gap:8px;margin-top:6px;font-family:"Open Sans",sans-serif;font-size:19px;color:var(--green)}

.nav-rule{left:92px;top:119px;width:904px;height:4px;background:var(--white)}
.nav{left:92px;top:127px;width:904px;height:42px;display:flex;background:linear-gradient(#f4f4f4,#dcdcdc)}
.nav a{display:flex;align-items:center;justify-content:center;font-size:15px;color:#333;text-decoration:none;border-left:1px solid #c9c9c9}
.nav a.active{background:var(--green);color:var(--white);border-left:none}

.panel{left:92px;top:169px;width:902px;height:919px;background:radial-gradient(ellipse at 40% 70%,#16508f 0%,var(--panel) 45%,var(--navy-deep) 100%)}

.slider{left:109px;top:180px;width:870px;height:332px;background:var(--white);padding:4px 4px 4px 6px}
.slide-photo{width:100%;height:100%;background:linear-gradient(100deg,#8fb0c4 0%,#d9c3ad 35%,#f1e7d6 60%,#b7cdd8 85%,#d9b8d4 100%)}
.slide-arrow{width:30px;height:34px;background:#000;display:flex;align-items:center;justify-content:center;top:311px}
.caption{left:733px;top:405px;width:243px;height:104px;background:rgba(255,255,255,.82);text-align:center;font-family:"Open Sans",sans-serif;font-size:26px;line-height:33px;color:var(--navy)}
.caption .lead{color:var(--green)}

.heading{font-family:"Open Sans",sans-serif;font-size:20px;font-weight:400;color:var(--white);letter-spacing:-.3px;white-space:nowrap}
.heading em{font-style:normal;color:var(--green)}
.dashed{height:0;border-top:1px dashed #9fb3cc}

.photo-frame{border:3px solid #b7c0cc}
.photo-back{background:linear-gradient(135deg,#c98f6c,#8d5a3e 60%,#3d4a62)}
.photo-hands{background:linear-gradient(135deg,#e8d7c7,#c59a7e 55%,#f1ece6)}

.intro{left:340px;top:619px;width:376px;font-size:11px;line-height:16.4px}
.intro p{margin-bottom:16px;text-align:justify}

.services{left:340px;top:893px;width:376px;list-style:none;font-size:11px;line-height:16.4px}
.services li{position:relative;padding-left:18px;margin-bottom:25px}
.services li::before{content:"»";position:absolute;left:0;top:0;font-weight:700}

.appointment{left:765px;top:583px;width:217px;height:238px;background:var(--box);border:1px solid #2a6aa8}
.appointment-photo{height:165px;background:linear-gradient(160deg,#d9ecf8,#7fb6dd 50%,#e9f2f8)}
.appointment-label{display:flex;align-items:center;justify-content:space-between;padding:10px 24px 0 25px;font-family:"Roboto Condensed",sans-serif;font-weight:700;font-size:20px;line-height:22px}

.testimonials{left:764px;top:838px;width:218px;height:238px;background:var(--box)}
.testimonials .heading{position:absolute;left:13px;top:15px;font-size:18px;letter-spacing:-.5px}
.testimonials .dashed{position:absolute;left:13px;top:44px;width:194px}
.quote{position:absolute;left:10px;width:198px;text-align:center;font-size:11px;line-height:16.4px}
.stars{display:flex;justify-content:center;gap:1px;margin:6px 0 6px 46px}
.byline{text-align:right;font-style:italic;padding-right:6px}

.footer{left:0;top:1088px;width:1088px;height:112px;background:linear-gradient(var(--footer-top),var(--footer-bottom))}
.stay{left:118px;top:1102px;font-family:"Open Sans",sans-serif;font-size:16px;color:var(--navy)}
.social{left:116px;top:1135px;display:flex;gap:11px}
.social span{width:37px;height:37px;border-radius:50%;background:var(--icon-dark);box-shadow:0 1px 2px rgba(0,0,0,.4);display:flex;align-items:center;justify-content:center}
.footer-links{right:116px;top:1120px;display:flex;gap:0;font-size:13px;color:#222}
.footer-links span.sep{margin:0 19px}
.copyright{right:116px;top:1162px;font-size:11.5px;color:#222}
</style>
</head>
<body>

<div class="abs brand"><span class="brand-dot"></span><span class="brand-name">Mosswood Chiropractic</span></div>

<div class="abs call">
  <div class="call-label">Call Now</div>
  <div class="call-number">
    <svg width="24" height="24" viewBox="0 0 24 24" aria-hidden="true"><circle cx="12" cy="12" r="12" fill="#e8e8e8"/><path d="M9 6.5c-.8 0-1.8 1-1.7 2.2.3 3.4 4.3 8 8 8.6 1.1.2 2-.8 2.1-1.6l-2.3-1.6-1.3 1c-1.5-.6-3.2-2.5-3.7-3.9l1-1.3z" fill="#3d4b3a"/></svg>
    <span>604-555-0182</span>
  </div>
</div>

<div class="abs nav-rule"></div>
<nav class="abs nav">
  <a class="active" style="width:179px" href="#">Home</a>
  <a style="width:187px" href="#">Aboout Us</a>
  <a style="width:189px" href="#">Services</a>
  <a style="width:189px" href="#">Testimonials</a>
  <a style="width:160px" href="#">Contact Us</a>
</nav>

<div class="abs panel"></div>

<div class="abs slider"><div class="slide-photo" role="img" aria-label="Smiling family of four sitting together outdoors in front of a house"></div></div>
<div class="abs slide-arrow" style="left:110px"><svg width="12" height="18" viewBox="0 0 12 18"><path d="M9 2 3 9l6 7" stroke="#fff" stroke-width="2.5" fill="none"/></svg></div>
<div class="abs slide-arrow" style="left:949px"><svg width="12" height="18" viewBox="0 0 12 18"><path d="M3 2l6 7-6 7" stroke="#fff" stroke-width="2.5" fill="none"/></svg></div>
<div class="abs caption"><span class="lead">Restoring Health</span><br>To<br>Your Body</div>

<h1 class="abs heading" style="left:118px;top:563px">WELCOME TO <em>MOSSWOOD CHIROPRACTIC</em></h1>
<div class="abs dashed" style="left:119px;top:597px;width:594px"></div>

<div class="abs photo-frame" style="left:119px;top:618px;width:206px;height:142px"><div class="photo-back" style="width:100%;height:100%" role="img" aria-label="Man holding his lower back in pain"></div></div>

<div class="abs intro">
  <p><b>Lorem Ipsum is simply dummy text of the printing and typesetting industry. Lorem Ipsum has been the industry's standard</b> dummy text ever since the 1500s,</p>
  <p>Lorem Ipsum is simply dummy text of the printing and typesetting industry. Lorem Ipsum has been the industry's stananged.Lorem Ipsum is simply dummy text of the printing and typesetting industry.</p>
  <p>&nbsp;Lorem Ipsum has been the industry's Lorem Ipsum is simply dummy text of the printing and typesetting industry.&nbsp; Lorem Ipsum has been the industry's Lorem Ipsum is simply dummy text of the printing and typesetting industry.</p>
</div>

<h2 class="abs heading" style="left:120px;top:821px">OUR <em>SERVICES</em></h2>
<div class="abs dashed" style="left:119px;top:855px;width:596px"></div>

<div class="abs photo-frame" style="left:119px;top:893px;width:207px;height:142px"><div class="photo-hands" style="width:100%;height:100%" role="img" aria-label="Chiropractor's hands adjusting a patient's lower back"></div></div>

<ul class="abs services">
  <li>Lorem Ipsum has been the industry's Lorem Ipsum is simply dummy text of the printing and typesetting industry.</li>
  <li>Lorem Ipsum has been the industry's Lorem Ipsum is simply dummy text of the printing and typesetting industry.</li>
  <li>Lorem Ipsum has been the industry's Lorem Ipsum is simply dummy text of the printing and typesetting industry.</li>
</ul>

<div class="abs appointment">
  <div class="appointment-photo" role="img" aria-label="Doctor in a white coat with arms crossed beside a spine model"></div>
  <div class="appointment-label">
    <span>Make An<br>Appointment</span>
    <svg width="56" height="56" viewBox="0 0 56 56" aria-hidden="true"><rect x="10" y="12" width="34" height="38" rx="4" fill="#fff" transform="rotate(18 27 31)"/><rect x="14" y="18" width="26" height="28" rx="2" fill="none" stroke="#0f4a86" stroke-width="2" transform="rotate(18 27 31)"/><circle cx="28" cy="31" r="7" fill="none" stroke="#0f4a86" stroke-width="2"/><path d="M28 27v4l3 2" stroke="#0f4a86" stroke-width="2" fill="none"/></svg>
  </div>
</div>

<section class="abs testimonials">
  <h3 class="heading">CLINTS <em>TESTIMONIALS</em></h3>
  <div class="dashed"></div>
  <div class="quote" style="top:62px">
    Lorem Ipsum is simply dummy text of the printing and typesetting industry.
    <div class="stars">
      <svg width="82" height="14" viewBox="0 0 82 14" aria-label="five stars"><g fill="var(--star)"><polygon points="7,0 9,5 14,5 10,8.5 11.5,14 7,10.5 2.5,14 4,8.5 0,5 5,5"/><polygon transform="translate(17 0)" points="7,0 9,5 14,5 10,8.5 11.5,14 7,10.5 2.5,14 4,8.5 0,5 5,5"/><polygon transform="translate(34 0)" points="7,0 9,5 14,5 10,8.5 11.5,14 7,10.5 2.5,14 4,8.5 0,5 5,5"/><polygon transform="translate(51 0)" points="7,0 9,5 14,5 10,8.5 11.5,14 7,10.5 2.5,14 4,8.5 0,5 5,5"/><polygon transform="translate(68 0)" points="7,0 9,5 14,5 10,8.5 11.5,14 7,10.5 2.5,14 4,8.5 0,5 5,5"/></g></svg>
    </div>
    <div class="byline">May 12, 2013 by Maren</div>
  </div>
  <div class="quote" style="top:146px">
    Lorem Ipsum is simply dummy text of the printing and typesetting industry.
    <div class="stars">
      <svg width="82" height="14" viewBox="0 0 82 14" aria-label="five stars"><g fill="var(--star)"><polygon points="7,0 9,5 14,5 10,8.5 11.5,14 7,10.5 2.5,14 4,8.5 0,5 5,5"/><polygon transform="translate(17 0)" points="7,0 9,5 14,5 10,8.5 11.5,14 7,10.5 2.5,14 4,8.5 0,5 5,5"/><polygon transform="translate(34 0)" points="7,0 9,5 14,5 10,8.5 11.5,14 7,10.5 2.5,14 4,8.5 0,5 5,5"/><polygon transform="translate(51 0)" points="7,0 9,5 14,5 10,8.5 11.5,14 7,10.5 2.5,14 4,8.5 0,5 5,5"/><polygon transform="translate(68 0)" points="7,0 9,5 14,5 10,8.5 11.5,14 7,10.5 2.5,14 4,8.5 0,5 5,5"/></g></svg>
    </div>
    <div class="byline">May 12, 2013 by Maren</div>
  </div>
</section>

<footer class="abs footer"></footer>
<div class="abs stay">Stay Connected</div>
<div class="abs social" aria-label="Social networks">
  <span aria-label="Share">
    <svg width="18" height="18" viewBox="0 0 18 18" aria-hidden="true"><g fill="#fff"><circle cx="4" cy="9" r="2.6"/><circle cx="14" cy="4" r="2.6"/><circle cx="14" cy="14" r="2.6"/></g><path d="M4 9 14 4M4 9l10 5" stroke="#fff" stroke-width="1.5"/></svg>
  </span>
  <span aria-label="Chat">
    <svg width="18" height="18" viewBox="0 0 18 18" aria-hidden="true"><path d="M2 3h14v9H7l-4 3v-3H2z" fill="#fff"/></svg>
  </span>
  <span aria-label="Email">
    <svg width="18" height="18" viewBox="0 0 18 18" aria-hidden="true"><rect x="2" y="4" width="14" height="10" rx="1" fill="#fff"/><path d="M2.5 4.5 9 10l6.5-5.5" stroke="#2b2b2b" stroke-width="1.4" fill="none"/></svg>
  </span>
  <span aria-label="Website">
    <svg width="18" height="18" viewBox="0 0 18 18" aria-hidden="true"><g stroke="#fff" stroke-width="1.5" fill="none"><circle cx="9" cy="9" r="7"/><ellipse cx="9" cy="9" rx="3" ry="7"/><path d="M2 9h14"/></g></svg>
  </span>
</div>
<div class="abs footer-links">
  <span>Home</span><span class="sep">-</span><span>Aboout Us</span><span class="sep" style="margin:0 22px 0 38px">-</span><span>Services</span><span class="sep">-</span><span>Testimonials</span><span class="sep">-</span><span>Contact Us</span>
</div>
<div class="abs copyright">Copyright (C)Mosswood Chiropractic 2013 - 2014 .&nbsp; All Rights Reserved</div>

</body>
</html>
```